New Business Cards for MB&LR

We need updated business cards for a staff of 15 engineers, estimators, project managers, and sales people. We have recently begun changes to our website and marketing material to improve our look and branding. We are an established fabricator specializing in pressure vessels, tanks, and structural steel. The owners require us to use the existing logo and old english text design. Also, we prefer dark grey or mostly black cards.
Target Market(s)
Engineers, purchasing agents, estimators, and project managers of; mining companies, refineries, industrial construction professionals
Industry/Entity Type
Business
Contact Information for Business Card
Logo, phone, website, email, etc.
Look and feel

```html
<!DOCTYPE html>
<html lang="en">
<head>
<meta charset="utf-8">
<title>MB&amp;LR Business Card</title>
<link href="https://fonts.googleapis.com/css2?family=Lato:wght@400;700&family=Libre+Baskerville&display=swap" rel="stylesheet">
<style>
  :root {
    --bg: #e9e6e1;
    --card-dark: #262626;
    --deboss: #3b3b3b;
    --card-light: #ffffff;
    --ink: #1a1a1a;
    --ink-soft: #333333;
    --rule: #111111;
  }
  * { margin: 0; padding: 0; box-sizing: border-box; }
  html, body { width: 1200px; height: 800px; overflow: hidden; background: var(--bg); }
  .canvas { position: relative; width: 1200px; height: 800px; }
  .card {
    position: absolute; left: 300px; width: 600px; height: 343px;
    border-radius: 22px; overflow: hidden;
    box-shadow: 0 4px 14px rgba(0,0,0,.18);
  }
  .card--front { top: 36px; background: var(--card-dark); }
  .card--back { top: 421px; background: var(--card-light); color: var(--ink); font-family: "Lato", sans-serif; }

  /* front */
  .front-brand {
    position: absolute; left: 70px; top: 0; bottom: 0;
    display: flex; align-items: center; gap: 34px;
  }
  .brand-mark { display: flex; align-items: center; gap: 10px; font-family: "Lato", sans-serif; font-weight: 700; font-size: 30px; color: var(--deboss); }
  .brand-mark .mark-square { width: 18px; height: 18px; background: var(--deboss); }
  .company-name {
    font-family: "Libre Baskerville", serif; font-size: 22px; line-height: 1.35;
    text-transform: uppercase; letter-spacing: 1px; color: var(--deboss);
  }

  /* back */
  .logo-block { position: absolute; right: 40px; top: 36px; display: flex; flex-direction: column; align-items: flex-end; gap: 14px; }
  .logo-block .brand-mark { color: var(--ink); font-size: 28px; }
  .logo-block .mark-square { background: var(--ink); }
  .badges { display: flex; gap: 8px; align-items: center; }
  .badge-round { width: 28px; height: 28px; border-radius: 50%; border: 2px solid var(--ink); }
  .badge-plate { width: 70px; height: 24px; border: 2px solid var(--ink); }

  .identity { position: absolute; left: 30px; top: 150px; padding-left: 14px; border-left: 7px solid var(--rule); }
  .identity .name { font-size: 25px; font-weight: 400; line-height: 1.05; }
  .identity .name strong { font-weight: 700; }
  .identity .title { font-size: 15px; color: var(--ink-soft); margin-top: 3px; }

  .rule { position: absolute; left: 300px; right: 0; top: 188px; height: 3px; background: var(--rule); }
  .website { position: absolute; right: 26px; top: 164px; font-size: 14px; color: var(--ink-soft); }

  .contacts { position: absolute; left: 52px; top: 218px; list-style: none; font-size: 15px; color: var(--ink-soft); }
  .contacts li { display: flex; align-items: flex-start; gap: 12px; line-height: 1.2; margin-bottom: 6px; }
  .contacts svg { width: 14px; height: 14px; flex: none; margin-top: 2px; fill: var(--ink-soft); }
</style>
</head>
<body>
<div class="canvas">
  <section class="card card--front">
    <div class="front-brand">
      <div class="brand-mark"><span class="mark-square"></span>MB&amp;LR</div>
      <p class="company-name">Meridian Beam &amp; Load Rail<br>Fabrication Company</p>
    </div>
  </section>

  <section class="card card--back">
    <div class="logo-block">
      <div class="brand-mark"><span class="mark-square"></span>MB&amp;LR</div>
      <div class="badges"><span class="badge-round"></span><span class="badge-plate"></span></div>
    </div>

    <div class="identity">
      <p class="name">Your <strong>Name</strong></p>
      <p class="title">Job title</p>
    </div>

    <div class="rule"></div>
    <p class="website">www.mbandlr.example</p>

    <ul class="contacts">
      <li>
        <svg viewBox="0 0 24 24"><path d="M12 2a7 7 0 0 0-7 7c0 5 7 13 7 13s7-8 7-13a7 7 0 0 0-7-7zm0 9.5A2.5 2.5 0 1 1 12 6.5a2.5 2.5 0 0 1 0 5z"/></svg>
        <span>48 East 200 South<br>P.O. Box 310288<br>Ridgeview, UT 84999-0288</span>
      </li>
      <li>
        <svg viewBox="0 0 24 24"><path d="M6.6 10.8a15 15 0 0 0 6.6 6.6l2.2-2.2a1 1 0 0 1 1-.25 11.4 11.4 0 0 0 3.6.57 1 1 0 0 1 1 1V20a1 1 0 0 1-1 1A17 17 0 0 1 3 4a1 1 0 0 1 1-1h3.5a1 1 0 0 1 1 1c0 1.25.2 2.45.57 3.57a1 1 0 0 1-.25 1z"/></svg>
        <span>555.014.2730</span>
      </li>
      <li>
        <svg viewBox="0 0 24 24"><path d="M6 3h10v5H6zM4 9h16a2 2 0 0 1 2 2v6h-4v4H6v-4H2v-6a2 2 0 0 1 2-2zm4 7v3h8v-3z"/></svg>
        <span>555.014.2731</span>
      </li>
      <li>
        <svg viewBox="0 0 24 24"><path d="M2 5h20v14H2zm2 2v.5l8 5 8-5V7z"/></svg>
        <span>youremail@xyz.com</span>
      </li>
    </ul>
  </section>
</div>
</body>
</html>
```